Hochwertiges Verpackungsdesign für Faltschachteln eines Online Shops gesucht
Zielgruppe
Wir sind eine Cannabis (CBD) Online Shop und suchen eine hochwertiges Design für Faltschachteln.
Aufgabenstellung
Es sollte hochwertig, elegant, modern und luxuriös sein, passend zum Firmenlogo. Es müssen folgende Sachen berücksichtigt werden: Das Design der Schachtel bleibt immer gleich aber es muss sich die Farbe wechsel für 4 verscheide Produkte und 4 verschiedene Namen der Produkte.
1. Design: Produktname: Kirschli- Farbe eher in Rottöne
2. Design: Produktname: Amber Leaf- Farbe eher in Orange-töne
3. Design: Produktname: K7- Farbe eher in Grün-töne
4. Design: Produktname: Frost Queen- Farbe eher in Grau / Silber
Die Schachteln müssen auch auf der Vorderseite 36% der Fläche und 51% auf der Rückseite einen Warnhinweis haben.
Folgende Daten müssen drauf sein:
THC < 1%
CBD < 8 % - 23 %
2.5gr - 24.95CHF
Sunny Meadow GmbH
Revers: 5169
www.sunnymeadow-shop.ch
100% Schweizer Indoor Hanfblüten
Produkt auf pflanzlicher Basis, ohne Tabak

```html
<!DOCTYPE html>
<html lang="de">
<head>
<meta charset="utf-8">
<title>Sunny Meadow – Faltschachteln</title>
<link rel="stylesheet" href="https://fonts.googleapis.com/css2?family=Didact+Gothic&family=Play:wght@400;700&family=Arimo:wght@400;700&display=swap">
<style>
:root{
  --ink:#111;
  --paper:#fff;
  --canvas:#ffffff;
  --line:#2a2a2a;
  --kirschli:#d99a8e;
  --kirschli-soft:#f3dcd8;
  --amber:#e0a54a;
  --amber-soft:#f6e5c8;
  --k7:#9cc07c;
  --k7-soft:#e6f2d8;
  --frost:#7fb6c6;
  --frost-soft:#dcedf2;
  --bud-dark:#5f7a3c;
  --bud-light:#c6d9a0;
  --warn-red:#e0322b;
  --help-blue:#1f6fc1;
}
*{box-sizing:border-box;margin:0;padding:0}
html,body{width:800px;height:1200px;overflow:hidden;background:var(--canvas)}
body{position:relative;font-family:"Didact Gothic",sans-serif;color:var(--ink)}

/* ---------- front panel range ---------- */
.range{position:absolute;left:30px;top:60px;width:740px;display:flex;gap:20px}
.front{position:relative;width:170px;height:216px;background:var(--ink);overflow:hidden}
.front.kirschli{--accent:var(--kirschli);--soft:var(--kirschli-soft)}
.front.amber{--accent:var(--amber);--soft:var(--amber-soft)}
.front.k7{--accent:var(--k7);--soft:var(--k7-soft)}
.front.frost{--accent:var(--frost);--soft:var(--frost-soft)}
.band{position:absolute;left:0;top:0;width:100%;height:70px;
  background:linear-gradient(135deg,var(--soft),#fff 55%,var(--soft))}
.age{position:absolute;left:6px;top:5px;font-size:14px}
.brand{position:absolute;left:0;right:0;display:flex;align-items:center;justify-content:center;gap:4px;font-family:"Didact Gothic",sans-serif}
.brand .dot{width:8px;height:8px;border-radius:50%;background:var(--ink)}
.front .brand{top:48px;font-size:11px}
.name{position:absolute;left:0;right:0;top:74px;text-align:center;font-family:"Play",sans-serif;font-weight:700;font-size:22px;letter-spacing:.5px;color:var(--accent);text-transform:uppercase}
.claim{position:absolute;left:0;right:0;text-align:center;color:var(--paper);font-size:8px;line-height:1.2}
.front .claim{top:101px}
.warnbox{position:absolute;left:8px;right:8px;background:var(--paper);color:var(--ink);text-align:center;font-family:"Arimo",sans-serif;font-size:6.4px;line-height:1.25;padding:5px 3px}
.front .warnbox{top:126px;bottom:8px}
.warnbox p+p{margin-top:3px}

/* ---------- dieline ---------- */
.dieline{position:absolute;left:40px;top:340px;width:720px;height:590px}
.panel{position:absolute;width:180px;border:1px solid var(--line);overflow:hidden;background:var(--ink)}
.panel .band{height:73px;--soft:var(--k7-soft);border-bottom:1px solid var(--line)}
.flap-top{left:180px;top:0;height:180px;
  background:linear-gradient(135deg,var(--k7-soft),#fff 55%,var(--k7-soft))}
.flap-top .brand{top:112px;font-size:18px}
.flap-top .brand .dot{width:12px;height:12px}
.side{top:180px;height:223px}
.p1{left:0}.p2{left:180px}.p3{left:360px}.p4{left:540px}
.flap-bottom{left:540px;top:403px;height:184px}
.spec{position:absolute;left:0;right:0;top:18px;text-align:center;font-size:11px}
.bud{position:absolute;left:44px;top:40px;width:92px;height:112px;border-radius:50%;
  background:radial-gradient(ellipse at 40% 40%,var(--bud-light),var(--bud-dark) 75%)}
.foot{position:absolute;left:0;right:0;bottom:12px;text-align:center;color:var(--paper);font-size:9px;line-height:1.25}
.p2 .age{font-size:15px}
.p2 .brand{top:52px;font-size:11px}
.p2 .name{top:76px;font-size:22px;font-family:"Didact Gothic",sans-serif;font-weight:400;color:var(--paper)}
.p2 .claim{top:103px}
.p2 .warnbox{top:128px;bottom:10px;left:18px;right:18px;font-size:6.6px}
.p4 .brand{top:50px;font-size:11px}
.backwarn{position:absolute;left:20px;right:20px;top:84px;color:var(--paper);font-family:"Arimo",sans-serif;font-weight:700;font-size:7px;line-height:1.2}
.backwarn p{margin-bottom:5px}
.backwarn .red{display:block;color:var(--warn-red);font-weight:400;font-size:6px}
.helpline{display:flex;align-items:center;gap:4px;background:var(--help-blue);color:var(--paper);font-family:"Arimo",sans-serif;font-weight:700;font-size:5.6px;line-height:1.2;padding:2px 4px;margin-top:2px}
.helpline svg{flex:none}
.imprint{position:absolute;left:0;right:0;top:62px;text-align:center;color:var(--paper);font-family:"Arimo",sans-serif;font-size:8px;line-height:1.3;transform:rotate(180deg)}
</style>
</head>
<body>

<section class="range">
  <article class="front kirschli">
    <div class="band" role="img" aria-label="Hanfblatt-Muster in Rosé"></div>
    <span class="age">18+</span>
    <div class="brand"><span class="dot"></span>Sunny Meadow</div>
    <h2 class="name">Kirschli</h2>
    <p class="claim">100%<br>SCHWEIZER INDOOR HANFBLÜTEN</p>
    <div class="warnbox">
      <p>Rauchen fügt Ihnen und den Menschen in Ihrer Umgebung erheblichen Schaden zu.</p>
      <p>Fumer nuit Gravement à votre santé et à celle de votre entourage.</p>
      <p>Il fumo daneggia gravemente te e chi ti sta intorno.</p>
    </div>
  </article>
  <article class="front amber">
    <div class="band" role="img" aria-label="Hanfblatt-Muster in Orange"></div>
    <span class="age">18+</span>
    <div class="brand"><span class="dot"></span>Sunny Meadow</div>
    <h2 class="name">Amber Leaf</h2>
    <p class="claim">100%<br>SCHWEIZER INDOOR HANFBLÜTEN</p>
    <div class="warnbox">
      <p>Rauchen fügt Ihnen und den Menschen in Ihrer Umgebung erheblichen Schaden zu.</p>
      <p>Fumer nuit Gravement à votre santé et à celle de votre entourage.</p>
      <p>Il fumo daneggia gravemente te e chi ti sta intorno.</p>
    </div>
  </article>
  <article class="front k7">
    <div class="band" role="img" aria-label="Hanfblatt-Muster in Grün"></div>
    <span class="age">18+</span>
    <div class="brand"><span class="dot"></span>Sunny Meadow</div>
    <h2 class="name">K7</h2>
    <p class="claim">100%<br>SCHWEIZER INDOOR HANFBLÜTEN</p>
    <div class="warnbox">
      <p>Rauchen fügt Ihnen und den Menschen in Ihrer Umgebung erheblichen Schaden zu.</p>
      <p>Fumer nuit Gravement à votre santé et à celle de votre entourage.</p>
      <p>Il fumo daneggia gravemente te e chi ti sta intorno.</p>
    </div>
  </article>
  <article class="front frost">
    <div class="band" role="img" aria-label="Hanfblatt-Muster in Eisblau"></div>
    <span class="age">18+</span>
    <div class="brand"><span class="dot"></span>Sunny Meadow</div>
    <h2 class="name">Frost Queen</h2>
    <p class="claim">100%<br>SCHWEIZER INDOOR HANFBLÜTEN</p>
    <div class="warnbox">
      <p>Rauchen fügt Ihnen und den Menschen in Ihrer Umgebung erheblichen Schaden zu.</p>
      <p>Fumer nuit Gravement à votre santé et à celle de votre entourage.</p>
      <p>Il fumo daneggia gravemente te e chi ti sta intorno.</p>
    </div>
  </article>
</section>

<section class="dieline">
  <div class="panel flap-top" role="img" aria-label="Deckel mit hellgrünem Hanfblatt-Muster">
    <div class="brand"><span class="dot"></span>Sunny Meadow</div>
  </div>

  <div class="panel side p1">
    <div class="band" role="img" aria-label="Hanfblatt-Muster in Grün"></div>
    <span class="spec">CBD&lt;8%-23%</span>
    <div class="bud" role="img" aria-label="Sichtfenster mit Hanfblüten"></div>
    <p class="foot">2.5 GR<br>24.95 CHF</p>
  </div>

  <div class="panel side p2">
    <div class="band" role="img" aria-label="Hanfblatt-Muster in Grün"></div>
    <span class="age">18+</span>
    <div class="brand"><span class="dot"></span>Sunny Meadow</div>
    <h2 class="name">K7</h2>
    <p class="claim">100%<br>SCHWEIZER INDOOR HANFBLÜTEN</p>
    <div class="warnbox">
      <p>Rauchen fügt Ihnen und den Menschen in Ihrer Umgebung erheblichen Schaden zu.</p>
      <p>Fumer nuit Gravement à votre santé et à celle de votre entourage.</p>
      <p>Il fumo daneggia gravemente te e chi ti sta intorno.</p>
    </div>
  </div>

  <div class="panel side p3">
    <div class="band" role="img" aria-label="Hanfblatt-Muster in Grün"></div>
    <span class="spec">THC&lt;1%</span>
    <div class="bud" role="img" aria-label="Sichtfenster mit Hanfblüten"></div>
    <p class="foot">PRODUKT AUF PFLANZLICHER BASIS<br>OHNE TABAK</p>
  </div>

  <div class="panel side p4">
    <div class="band" role="img" aria-label="Hanfblatt-Muster in Grün"></div>
    <div class="brand"><span class="dot"></span>Sunny Meadow</div>
    <div class="backwarn">
      <p>Lebenslange Raucher verlieren im Durchschnitt 14 Jahre ihres Lebens.<span class="red">Wenn Sie rauchen, sterben Sie früher.</span></p>
      <p>Continuez à fumer, et vous risquez de perdre 14 années de vie.<span class="red">Fumer, c'est vivre moins longtemps.</span></p>
      <p>I fumatori cronici perdono una media di 14 anni di vita.<span class="red">I fumatori muoiono prima.</span></p>
      <div class="helpline">
        <svg width="10" height="10" viewBox="0 0 10 10" aria-hidden="true"><path d="M1.5 5.5 L4 8 L8.5 1.5" fill="none" stroke="#fff" stroke-width="1.6"/></svg>
        <span>Hilfelinie/Ligne d'aide/<br>Linea d'aiuto 0848 123 456</span>
      </div>
    </div>
  </div>

  <div class="panel flap-bottom">
    <p class="imprint">SUNNY MEADOW GMBH<br>REVERS: 5169<br>WWW.SUNNYMEADOW-SHOP.CH</p>
  </div>
</section>

</body>
</html>
```